Website Refresh for Meadowbrook Childcare

Company Overview:

Meadowbrook Childcare is a trusted provider of early childhood education and care services. We are dedicated to creating a nurturing environment where children can grow, learn, and thrive. Our centres offer a range of programs tailored to different age groups, and we pride ourselves on our commitment to quality, safety, and community engagement.

Project Overview:

We are looking for a talented designer to refresh our existing website (https://meadowbrookchildcare.com.au/).

The primary goal is to modernize the design while keeping the content unchanged. The new design should be user-friendly, visually appealing, and reflective of our brand’s values. The website should share a similar "DNA" with our sister company’s website, Tindle Grove Early Learning, (https://tindlegroveelc.com.au/) but it should not be a direct copy.

We want a design that mirrors our brand's shared values while introducing unique elements that distinguish Meadowbrook Childcare.

Design Requirements:
1. Home Page
2. About Us
3. Parent Info
4. Our Programs
5. Template for Centre Pages
6. Contact Us / Enrolment (Optional)

Design Style and Inspiration:
• The design should align with the "DNA" of Tindle Grove Early Learning, but also bring in unique design elements to set Meadowbrook Childcare apart.
• We are looking for a clean, modern, and professional design that is easy to navigate.
• The colour scheme and design elements should reflect our brand’s identity—welcoming, warm, and child-friendly without being overly childish.
• The design must be responsive, ensuring a great user experience across all devices, including desktops, tablets, and mobile phones.
• Accessibility is crucial—use clear fonts, sufficient contrast, and straightforward navigation.

Content Considerations:
• The content will remain the same; the focus is on enhancing the design and user interface.

Deliverables:
• High-fidelity mock-ups for each of the specified pages.
• Responsive design layouts for desktop, tablet, and mobile views.
• Design files should be delivered in a format compatible with any development team.

Target Audience:
• Parents of young children looking for childcare services.
• Community members interested in learning more about our centres and programs.

Submission Requirements:
• A brief explanation of your design approach and how it aligns with our branding goals.
• A portfolio showcasing your previous work, especially any similar projects.
• All requested deliverables must be included in your submission.

Judging Criteria:
• Alignment with our brand identity and the "DNA" of our sister company’s website.
• Visual appeal and user-friendliness of the design.
• Responsiveness and adaptability across different devices.
• Creativity and uniqueness in differentiating Meadowbrook Childcare from our sister company.

Notes:
• While we would like to engage the winning artist with the coding / css work, its not mandatory.
• Feel free to ask for any digital assets you need to complete the work.
• Main site to be refreshed - https://meadowbrookchildcare.com.au/
• Sister site to take inspiration from - https://tindlegroveelc.com.au/

Target Market(s)

A) Parents of young children looking for childcare services. B)Community members interested in learning more about our centres and programs.

Industry/Entity Type

Child Care

Number of Pages Required

5+ page

Requirements
Must have
• Please read description
Nice to have
• Please read description
Should not have
• Please read description

```html
<!DOCTYPE html>
<html lang="en">
<head>
<meta charset="utf-8">
<title>About Us – Meadowbrook Early Learning Centre</title>
<link href="https://fonts.googleapis.com/css2?family=Figtree:wght@400;500;600&family=Lora:wght@500;600&display=swap" rel="stylesheet">
<style>
:root{
  --cream:#fbfaf4;
  --green:#1e4722;
  --green-soft:#285a2d;
  --green-brand:#3a9a2e;
  --grey:#e8e8e6;
  --grey-soft:#f1f1ee;
  --ink:#1e4722;
  --white:#ffffff;
}
*{box-sizing:border-box;margin:0;padding:0}
html,body{width:1200px;height:3217px;overflow:hidden}
body{position:relative;background:var(--cream);font-family:"Figtree",sans-serif;color:var(--ink)}
.abs{position:absolute}
.serif{font-family:"Lora",serif}

/* header */
.site-header{left:0;top:0;width:1200px;height:70px}
.brand{left:56px;top:16px;display:flex;align-items:center;gap:8px;font-family:"Figtree",sans-serif;font-weight:600;font-size:22px;color:var(--green-brand)}
.brand-dot{width:18px;height:18px;border-radius:50%;background:var(--green-brand)}
.main-nav{right:56px;top:22px;display:flex;gap:27px;font-size:9px;font-weight:500}
.main-nav a{color:var(--ink);text-decoration:none;padding-bottom:4px}
.main-nav a.active{border-bottom:2px solid var(--ink)}

.page-title{left:0;width:1200px;top:86px;text-align:center;font-size:56px;font-weight:600;color:var(--green)}

/* hero */
.hero-bg{left:0;top:200px;width:1200px;height:500px}
.hero-photo{left:91px;top:218px;width:1020px;height:427px;border-radius:26px;background:linear-gradient(100deg,#d9d4cf 0%,#c9c8c9 40%,#b9bec4 70%,#d8d2cc 100%)}

/* intro */
.intro{left:0;top:697px;width:1200px;height:443px;background:var(--green);overflow:hidden}
.intro-line{left:84px;top:96px;width:1px;height:252px;background:rgba(255,255,255,.6)}
.intro-text{left:139px;top:66px;width:950px;color:var(--white);font-size:16.6px;line-height:22.5px;font-weight:500}
.intro-text p+p{margin-top:22.5px}

/* orgs */
.orgs-kicker{left:0;width:1200px;top:1202px;text-align:center;font-size:17px;font-weight:500}
.orgs-title{left:0;width:1200px;top:1226px;text-align:center;font-size:35px;font-weight:600}
.pill-row{left:0;width:1200px;display:flex;justify-content:center;gap:27px}
.pill{height:38px;padding:0 11px;border:2.5px solid var(--green);border-radius:20px;display:flex;align-items:center;font-size:16.5px;font-weight:500;color:var(--green);white-space:nowrap}
.btn{height:42px;padding:0 12px;border-radius:22px;display:flex;align-items:center;font-size:17px;font-weight:500}
.btn-dark{background:var(--green);color:var(--white)}
.enquire{left:512px;top:1363px}

/* team */
.team{left:0;top:1474px;width:1200px;height:831px;background:var(--green);overflow:hidden}
.team-photo{left:84px;top:66px;width:1024px;height:281px;border-radius:24px;background:linear-gradient(90deg,#6d6c6a 0%,#7b7976 50%,#6b6a68 100%)}
.team-title{left:84px;top:402px;font-size:37px;font-weight:600;color:var(--white)}
.team-text{left:84px;top:465px;width:1030px;color:var(--white);font-size:17px;line-height:22.5px;font-weight:500}
.team-text p+p{margin-top:22.5px}
.team-actions{left:84px;top:716px;display:flex;gap:23px}
.btn-light{background:var(--white);color:var(--green);height:48px;border-radius:26px;padding:0 13px}
.btn-outline{border:2.5px solid var(--white);color:var(--white);height:48px;border-radius:26px;padding:0 12px}

/* partners */
.partners-title{left:0;width:1200px;top:2368px;text-align:center;font-size:37px;font-weight:600}
.pp{height:48px;border-radius:26px;font-size:17.5px;padding:0 12px}
.pill.on{background:var(--green);color:var(--white)}
.partner-name{left:0;width:1200px;top:2662px;text-align:center;font-size:27px;font-weight:500}
.partner-desc{left:0;width:1200px;top:2724px;text-align:center;font-size:17.5px;font-weight:500}

/* footer */
.footer-bg{left:0;top:2810px;width:1200px;height:407px}
.footer-brand{left:56px;top:2898px}
.badge-training{left:248px;top:2866px;width:80px;height:70px;border-radius:6px;background:#e6dcdc}
.badge-kinder{left:74px;top:2972px;width:222px;height:54px;border-radius:8px;background:#e9eef7;border:2px solid #c9d3e6}
.footer-col{top:2918px}
.footer-col h3{font-size:22px;font-weight:500;margin-bottom:18px}
.footer-col a{display:block;color:var(--ink);text-decoration:none;font-size:14.5px;font-weight:500;line-height:36px}
.socials{left:66px;top:3112px;display:flex;gap:27px}
.social{width:26px;height:26px;border-radius:50%;border:2.5px solid var(--ink)}
.copyright{left:68px;top:3165px;font-size:14px}
</style>
</head>
<body>

<header class="site-header abs">
  <div class="brand abs"><span class="brand-dot"></span>Meadowbrook</div>
  <nav class="main-nav abs">
    <a href="#">Home</a><a href="#" class="active">About Us</a><a href="#">Parent Information</a><a href="#">Our Programs</a><a href="#">Our Centres</a><a href="#">Contact</a><a href="#">Enroll</a>
  </nav>
</header>

<h1 class="page-title abs serif">About Us</h1>

<svg class="hero-bg abs" viewBox="0 0 1200 500" aria-hidden="true">
  <path d="M0 500 L0 420 C60 260 120 120 300 60 L1120 10 C1160 5 1190 15 1200 30 L1200 500 Z" fill="var(--grey)"/>
</svg>
<div class="hero-photo abs" role="img" aria-label="Young children drawing at tables in a bright classroom"></div>

<section class="intro abs">
  <svg class="abs" style="left:0;top:0" width="1200" height="443" viewBox="0 0 1200 443" aria-hidden="true">
    <path d="M0 443 C80 320 200 250 420 220 L1200 200 L1200 0 L1180 0 C1100 60 1000 90 700 120 C300 160 80 260 0 380 Z" fill="var(--green-soft)" opacity=".35"/>
  </svg>
  <div class="intro-line abs"></div>
  <div class="intro-text abs">
    <p>The Meadowbrook Group is family owned and operated. We have been providing quality care and education since 2003. Each Centre in the group has its own unique character and offers services that reflect the local communities in which they are located. Our Centres are licensed by the National Children’s Care Standards Board (NCCSB) and are governed by the Office of Early Years Learning and Care.</p>
    <p>The Meadowbrook Group is committed to providing inclusive environments for all children and families. Underpinning this value is our fundamental belief that each child is unique, bringing to the environment a unique set of capabilities and pre-dispositions. Our aim is to foster within each child an awareness and acceptance of others so that they attach positive feelings to the diversity of people.</p>
    <p>Of paramount importance is the provision of high-quality care which we believe is the right of every child. By providing a socially just program, stimulating experiences and positive interactions, all aspects of a child’s learning and development is facilitated in order to support each family’s efforts in raising their child to become competent and confident learners with skills to equip them for lifelong learning.</p>
  </div>
</section>

<p class="orgs-kicker abs serif">Meadowbrook are Members of the following</p>
<h2 class="orgs-title abs serif">Professional Organisations:</h2>
<div class="pill-row abs" style="top:1298px">
  <span class="pill">PLCN</span>
  <span class="pill">EARLY YEARS ALLIANCE NETWORK</span>
  <span class="pill">THE ATELIER LEARNING EXCHANGE</span>
  <span class="pill">HEALTHY PLATES COLLECTIVE</span>
</div>
<a class="btn btn-dark enquire abs">Enquire Now</a>

<section class="team abs">
  <svg class="abs" style="left:0;top:0" width="1200" height="831" viewBox="0 0 1200 831" aria-hidden="true">
    <path d="M0 831 C40 600 60 400 200 300 L1200 260 L1200 0 L1140 0 C1060 40 1040 120 900 160 L0 200 Z" fill="var(--green-soft)" opacity=".3"/>
  </svg>
  <div class="team-photo abs" role="img" aria-label="Group of smiling early childhood educators"></div>
  <h2 class="team-title abs serif">Our Team</h2>
  <div class="team-text abs">
    <p>Our Early Childhood Educators are professionally trained to provide children with a warm, caring atmosphere where a child can feel safe and welcome. At Meadowbrook we strongly believe that it is important for Educators to keep up to date with new trends, developments, and practices. At Meadowbrook we provide regular in-service training and professional development opportunities for our staff. We believe this ongoing training is highly important for staff professional development as it enables us to offer a high-quality service.</p>
    <p>All of our Educators are dedicated to providing your child with quality education and care. Our Management, Early Childhood Teachers and Lead Educators all have an approved qualification in Early Childhood Education. All staff are required to hold a current blue card issued by the Commission for Child Safety and Wellbeing, in addition to that, all staff must have current First Aid and CPR Certificates which includes Anaphylaxis and Asthma Training.</p>
  </div>
  <div class="team-actions abs">
    <a class="btn btn-light">Our Programs</a>
    <a class="btn btn-outline">Parents Info</a>
  </div>
</section>

<h2 class="partners-title abs serif">Some of Our Extra Curricular Partners</h2>
<div class="pill-row abs" style="top:2456px">
  <span class="pill pp on">Open Canvas</span>
  <span class="pill pp">Melody Makers</span>
  <span class="pill pp">Jumpabout</span>
  <span class="pill pp">Sprout Sports</span>
  <span class="pill pp">Tiny Steps Dance</span>
  <span class="pill pp">Little Aces Tennis</span>
</div>
<div class="pill-row abs" style="top:2532px">
  <span class="pill pp">Active Kids</span>
  <span class="pill pp">Brave Hearts Rugby</span>
  <span class="pill pp">Dance Classes</span>
</div>
<h3 class="partner-name abs">Open Canvas</h3>
<p class="partner-desc abs">3-5 years, focusing on developing children’s creativity&nbsp; expressing themselves through open ended art experiences.</p>

<footer>
  <svg class="footer-bg abs" viewBox="0 0 1200 407" aria-hidden="true">
    <path d="M0 0 C150 40 300 120 500 150 C700 180 850 120 1000 160 C1120 190 1180 300 1200 407 L0 407 Z" fill="var(--grey-soft)"/>
  </svg>
  <div class="brand footer-brand abs" style="font-size:26px"><span class="brand-dot" style="width:22px;height:22px"></span>Meadowbrook</div>
  <div class="badge-training abs" role="img" aria-label="Training accreditation badge"></div>
  <div class="badge-kinder abs" role="img" aria-label="Approved kindergarten program badge"></div>
  <div class="footer-col abs" style="left:586px">
    <h3>Quick Links Parents</h3>
    <a href="#">Our Programs</a><a href="#">Parent Information</a><a href="#">About Us</a><a href="#">Contact</a><a href="#">Our Centres</a>
  </div>
  <div class="footer-col abs" style="left:857px">
    <h3>Quick Links Educators</h3>
    <a href="#">RTO</a><a href="#">Careers</a><a href="#">Our Centres</a><a href="#">About Us</a><a href="#">Our Programs</a>
  </div>
  <div class="socials abs">
    <span class="social" role="img" aria-label="Social profile link"></span>
    <span class="social" role="img" aria-label="Social profile link"></span>
    <span class="social" role="img" aria-label="Social profile link"></span>
  </div>
  <p class="copyright abs">© 2024 Meadowbrook Early Learning Centre.&nbsp; All rights reserved.</p>
</footer>

</body>
</html>
```